Icons/images for company values

We have five company values, we have a new logo and a new look. I would like drawn images for each value that are in keeping with our look and feel.

Target Market(s)

internal/staff

Industry/Entity Type

media compliance

Requirements
Must have
• colours aligned with logo.

```html
<!DOCTYPE html>
<html lang="en">
<head>
<meta charset="utf-8">
<title>Norvale Values 2023</title>
<link rel="stylesheet" href="https://fonts.googleapis.com/css2?family=Jost:wght@400;500&family=Poppins:wght@400;700;800&display=swap">
<style>
  :root {
    --navy: #0d6a8f;
    --blue: #1a7fbf;
    --sky: #1e96cf;
    --teal: #3fc9b0;
    --lime: #8fd07a;
    --yellow: #e8c21a;
    --ink: #111418;
    --rule: #8fb3c9;
    --paper: #ffffff;
  }
  html, body {
    margin: 0;
    width: 1200px;
    height: 1200px;
    overflow: hidden;
    background: var(--paper);
  }
  .sheet {
    position: absolute;
    left: 0;
    top: 136px;
    width: 1246px;
    height: 964px;
    transform: scale(0.963);
    transform-origin: 0 0;
    font-family: "Poppins", sans-serif;
    color: var(--ink);
  }
  .wheel {
    position: absolute;
    left: 0;
    top: 0;
  }
  .brand-name {
    position: absolute;
    left: 58px;
    top: 176px;
    font-family: "Jost", sans-serif;
    font-weight: 400;
    font-size: 42px;
    letter-spacing: 8px;
    color: var(--blue);
    margin: 0;
  }
  .value {
    position: absolute;
  }
  .value h2 {
    margin: 0;
    font-weight: 800;
    font-size: 27px;
    line-height: 31px;
    text-transform: uppercase;
    letter-spacing: 0.3px;
  }
  .value p {
    margin: 0;
    font-size: 18px;
    line-height: 23px;
    font-weight: 400;
  }
  .value--open { left: 486px; top: 86px; }
  .value--open h2 { color: var(--navy); }
  .value--open p { margin-top: 4px; }
  .value--together { left: 642px; top: 232px; }
  .value--together h2 { color: var(--sky); }
  .value--together p { margin-top: 4px; }
  .value--leaders { left: 690px; top: 410px; }
  .value--leaders h2 { color: var(--teal); }
  .value--leaders p { margin-top: 14px; }
  .value--done { left: 642px; top: 650px; }
  .value--done h2 { color: var(--lime); }
  .value--done p { margin-top: 4px; }
  .value--diverse { left: 486px; top: 789px; }
  .value--diverse h2 { color: var(--yellow); }
  .value--diverse p { margin-top: 4px; }
  .divider {
    position: absolute;
    height: 0;
    border-top: 1.5px dotted var(--rule);
  }
  .divider--1 { left: 580px; width: 555px; top: 193px; }
  .divider--2 { left: 630px; width: 505px; top: 359px; }
  .divider--3 { left: 630px; width: 505px; top: 607px; }
  .divider--4 { left: 570px; width: 565px; top: 760px; }
</style>
</head>
<body>
<main class="sheet">
  <p class="brand-name">NORVALE</p>

  <svg class="wheel" width="700" height="964" viewBox="0 0 700 964" aria-label="Values wheel">
    <defs>
      <linearGradient id="seg-open" x1="0" y1="0" x2="1" y2="1">
        <stop offset="0" stop-color="#0b5f8e"/>
        <stop offset="1" stop-color="#1582c2"/>
      </linearGradient>
      <linearGradient id="seg-together" x1="0" y1="0" x2="1" y2="1">
        <stop offset="0" stop-color="#1b8fd2"/>
        <stop offset="1" stop-color="#36b6bb"/>
      </linearGradient>
      <linearGradient id="seg-leaders" x1="0" y1="0" x2="1" y2="1">
        <stop offset="0" stop-color="#3cc6b8"/>
        <stop offset="1" stop-color="#62dca6"/>
      </linearGradient>
      <linearGradient id="seg-done" x1="1" y1="0" x2="0" y2="1">
        <stop offset="0" stop-color="#86d98e"/>
        <stop offset="1" stop-color="#e2e05a"/>
      </linearGradient>
    </defs>

    <g class="segments" stroke="#ffffff" stroke-width="10" stroke-linejoin="miter">
      <path fill="url(#seg-open)" d="M274 287 L274 130 A340 340 0 0 1 473.9 194.9 L381.6 322 A183 183 0 0 0 274 287 Z"/>
      <path fill="url(#seg-together)" d="M381.6 322 L473.9 194.9 A340 340 0 0 1 597.4 364.9 L448 413.5 A183 183 0 0 0 381.6 322 Z"/>
      <path fill="url(#seg-leaders)" d="M448 413.5 L597.4 364.9 A340 340 0 0 1 597.4 575.1 L448 526.5 A183 183 0 0 0 448 413.5 Z"/>
      <path fill="url(#seg-done)" d="M448 526.5 L597.4 575.1 A340 340 0 0 1 473.9 745.1 L381.6 618 A183 183 0 0 0 448 526.5 Z"/>
      <path fill="#edc91a" d="M381.6 618 L473.9 745.1 A340 340 0 0 1 274 810 L274 653 A183 183 0 0 0 381.6 618 Z"/>
    </g>

    <g class="value-icons" fill="#ffffff" fill-opacity="0.28">
      <rect x="315" y="181" width="80" height="80" rx="14" role="img" aria-label="Icon: two colleagues talking"/>
      <rect x="446" y="276" width="80" height="80" rx="14" role="img" aria-label="Icon: stopwatch inside circular arrows"/>
      <rect x="496" y="430" width="80" height="80" rx="14" role="img" aria-label="Icon: lightbulb with a tick"/>
      <rect x="446" y="584" width="80" height="80" rx="14" role="img" aria-label="Icon: head with a gear"/>
      <rect x="315" y="679" width="80" height="80" rx="14" role="img" aria-label="Icon: hands joined together"/>
    </g>

    <circle cx="274" cy="470" r="183" fill="#ffffff" stroke="#9cc6cf" stroke-width="1.2"/>
    <circle cx="274" cy="470" r="156" fill="var(--navy)"/>
    <text x="274" y="455" text-anchor="middle" fill="#ffffff" font-family="Jost, sans-serif" font-weight="400" font-size="56">VALUES</text>
    <text x="274" y="525" text-anchor="middle" fill="#ffffff" font-family="Jost, sans-serif" font-weight="500" font-size="80">2023</text>
  </svg>

  <section class="value value--open">
    <h2>We're open and honest</h2>
    <p>Sharing information helps us achieve the best outcomes for our teams<br>and business. We value open, honest, and clear communication.</p>
  </section>
  <div class="divider divider--1"></div>

  <section class="value value--together">
    <h2>We get &nbsp;there faster together</h2>
    <p>Collaboration is at the heart of what we do, no<br>matter our team.</p>
  </section>
  <div class="divider divider--2"></div>

  <section class="value value--leaders">
    <h2>We are leaders in copyright<br>and intellectual property</h2>
    <p>Leading the conversation in audio-visual<br>copyright compliance and advocating for<br>the protection of intellectual property globally.</p>
  </section>
  <div class="divider divider--3"></div>

  <section class="value value--done">
    <h2>We get things done</h2>
    <p>We grow through capability, focus and hard work. We<br>believe small steps compound to big results.</p>
  </section>
  <div class="divider divider--4"></div>

  <section class="value value--diverse">
    <h2>Diverse perspectives build better outcomes</h2>
    <p>We value diversity, inclusion, respect and trust within our teams. We are<br>building a truly global organisation.</p>
  </section>
</main>
</body>
</html>
```